Geschäftspapiere für Rechtsanwalt Jan Brückner
Zielgruppe
Rechtsanwaltskanzlei mit Schwerpunkt im Strafrecht - Fachanwalt für Strafrecht
Weiterer Schwerpunkt - Hochschul- und Prüfungsrecht, also insbesondere Studenten und Schulabgänger die studieren möchten.
Aufgabenstellung
Keine - Einfach drauflos - Ich bin gespannt

```html
<!DOCTYPE html>
<html lang="de">
<head>
<meta charset="utf-8">
<title>Geschäftspapiere – Jan Brückner, Fachanwalt für Strafrecht</title>
<link rel="stylesheet" href="https://fonts.googleapis.com/css2?family=Montserrat:wght@400;500;600;700&display=swap">
<style>
  :root {
    --ink: #0b0b0b;
    --paper: #ffffff;
    --ground: #c8c8ca;
    --mark: #a9a9ab;
    --body-text: #2a2a2a;
    --rule: #d8d8d8;
  }
  * { box-sizing: border-box; margin: 0; padding: 0; }
  html, body { width: 1200px; height: 2400px; overflow: hidden; }
  body {
    background: var(--ground);
    font-family: "Montserrat", Arial, sans-serif;
    color: var(--ink);
    position: relative;
  }
  .piece { position: absolute; box-shadow: 0 2px 6px rgba(0,0,0,.18); }

  /* Brand signature: name + plain circle */
  .brand { display: flex; flex-direction: column; align-items: center; text-align: center; }
  .brand-dot { border-radius: 50%; background: var(--mark); }
  .brand-name { font-weight: 700; letter-spacing: .04em; text-transform: uppercase; }
  .brand-role { font-weight: 400; }

  /* Business cards */
  .card { width: 460px; height: 280px; }
  .card-front { background: var(--ink); color: var(--paper); left: 110px; top: 320px; }
  .card-back { background: var(--paper); left: 630px; top: 320px; }
  .card-front .claim {
    position: absolute; top: 120px; width: 100%; text-align: center;
    font-weight: 600; font-size: 17px; letter-spacing: .04em;
  }
  .card-front .phone {
    position: absolute; bottom: 26px; width: 100%; text-align: center;
    font-weight: 600; font-size: 15px; letter-spacing: .03em;
  }
  .card-back .brand { padding-top: 56px; }
  .card-back .brand-dot { width: 52px; height: 52px; margin-bottom: 12px; }
  .card-back .brand-name { font-size: 16px; }
  .card-back .brand-role { font-size: 13px; margin-top: 2px; }
  .card-back .address { margin-top: 24px; font-size: 11px; line-height: 1.55; color: #333; }

  /* Folder */
  .folder { background: var(--ink); color: var(--paper); width: 330px; height: 460px; left: 140px; top: 1290px; }
  .folder .claim { position: absolute; top: 182px; width: 100%; text-align: center; font-weight: 600; font-size: 14px; letter-spacing: .04em; }
  .folder .owner { position: absolute; bottom: 26px; width: 100%; text-align: center; font-weight: 600; font-size: 8px; letter-spacing: .06em; }

  /* Letterhead */
  .letter { background: var(--paper); width: 320px; height: 452px; left: 496px; top: 1294px; }
  .letter .brand { padding-top: 34px; }
  .letter .brand-dot { width: 20px; height: 20px; margin-bottom: 4px; }
  .letter .brand-name { font-size: 6px; }
  .letter .brand-role { font-size: 5px; }
  .letter .recipient { position: absolute; left: 46px; top: 102px; font-size: 5px; line-height: 1.35; }
  .letter .fold { position: absolute; left: 6px; top: 148px; width: 14px; border-top: 1px solid #999; }
  .letter .text { position: absolute; left: 46px; right: 44px; top: 170px; font-size: 5px; line-height: 1.4; color: var(--body-text); }
  .letter .text p { margin-bottom: 6px; }
  .letter .sender { position: absolute; left: 46px; top: 340px; font-size: 5px; line-height: 1.35; }
  .letter .footer { position: absolute; bottom: 18px; width: 100%; text-align: center; font-size: 4.5px; line-height: 1.4; }

  /* Badge card and compliment card */
  .mini-front { background: var(--ink); color: var(--paper); width: 140px; height: 84px; left: 848px; top: 1590px; }
  .mini-front .claim { position: absolute; top: 34px; width: 100%; text-align: center; font-size: 5px; font-weight: 600; letter-spacing: .04em; }
  .mini-front .phone { position: absolute; bottom: 8px; width: 100%; text-align: center; font-size: 4.5px; font-weight: 600; }
  .mini-back { background: var(--paper); width: 128px; height: 82px; left: 844px; top: 1678px; }
  .mini-back .brand { padding-top: 14px; }
  .mini-back .brand-dot { width: 14px; height: 14px; margin-bottom: 3px; }
  .mini-back .brand-name { font-size: 4.5px; }
  .mini-back .brand-role { font-size: 4px; }
  .mini-back .address { margin-top: 6px; font-size: 3.5px; line-height: 1.4; }

  /* Square flyer */
  .flyer { background: var(--ink); color: var(--paper); width: 198px; height: 198px; left: 144px; top: 1770px; }
  .flyer .claim { position: absolute; top: 94px; width: 100%; text-align: center; font-weight: 600; font-size: 9px; letter-spacing: .04em; }
  .flyer .owner { position: absolute; bottom: 14px; width: 100%; text-align: center; font-weight: 600; font-size: 5px; letter-spacing: .06em; }

  /* Disc */
  .disc { left: 352px; top: 1784px; width: 182px; height: 182px; box-shadow: none; }
  .disc .brand { position: absolute; top: 16px; width: 100%; }
  .disc .brand-dot { width: 16px; height: 16px; margin-bottom: 3px; }
  .disc .brand-name { font-size: 5.5px; }

  /* Envelopes */
  .envelope-back { background: var(--paper); width: 334px; height: 166px; left: 732px; top: 1756px; }
  .envelope-back .flap { position: absolute; left: 0; right: 0; top: 22px; border-top: 1px solid var(--rule); }
  .envelope { background: var(--paper); width: 332px; height: 166px; left: 570px; top: 1806px; }
  .envelope .brand { padding-top: 14px; }
  .envelope .brand-dot { width: 22px; height: 22px; margin-bottom: 4px; }
  .envelope .brand-name { font-size: 6px; }
  .envelope .sender-block { position: absolute; left: 14px; top: 102px; font-size: 4px; line-height: 1.4; }
  .envelope .sender-block strong { font-weight: 700; }
  .envelope .window { position: absolute; left: 220px; top: 84px; width: 96px; height: 58px; }
</style>
</head>
<body>

  <!-- Business card, front -->
  <section class="piece card card-front" aria-label="Visitenkarte Vorderseite">
    <p class="claim">KANN NUR BESSER WERDEN</p>
    <p class="phone">0176 . 48 21 90 35</p>
  </section>

  <!-- Business card, back -->
  <section class="piece card card-back" aria-label="Visitenkarte Rückseite">
    <div class="brand">
      <span class="brand-dot"></span>
      <span class="brand-name">Jan Brückner</span>
      <span class="brand-role">Fachanwalt für Strafrecht</span>
      <p class="address">Rechtsanwaltskanzlei mit Schwerpunkt Strafrecht<br>Lindenweg 14 · 22587 Hamburg · jb@kanzlei-janbrueckner.de</p>
    </div>
  </section>

  <!-- Folder -->
  <section class="piece folder" aria-label="Mappe">
    <p class="claim">KANN NUR BESSER WERDEN</p>
    <p class="owner">JAN BRÜCKNER</p>
  </section>

  <!-- Letterhead -->
  <section class="piece letter" aria-label="Briefbogen">
    <div class="brand">
      <span class="brand-dot"></span>
      <span class="brand-name">Jan Brückner</span>
      <span class="brand-role">Fachanwalt für Strafrecht</span>
    </div>
    <p class="recipient">First Name Last Name<br>Addressee's name<br>Building number/name and street<br>Post Town, Post Code</p>
    <span class="fold"></span>
    <div class="text">
      <p>Dear First Name</p>
      <p>Lorem ipsum dolor sit amet, consectetur adipiscing elit. Vestibulum eu vulputate sapien. In quis imperdiet lectus, eget accumsan sem. Vestibulum consequat rhoncus cursus. Quisque ultrices facilisis libero, eu facilisis nisl congue sit amet. Phasellus consequat justo mi. In sollicitudin justo sed eros blandit, non eleifend elit faucibus. Aliquam elit purus, facilisis at pulvinar eu, rutrum ut mauris. Suspendisse aliquam ipsum vitae egestas venenatis. Quisque a lacinia orci, sit amet tincidunt diam. Nulla blandit justo sit amet purus gravida, pulvinar iaculis sapien egestas. Sed vehicula diam leo, et vehicula leo elementum et. Duis nec suscipit justo. Maecenas eget pretium leo. Quisque imperdiet ut quam ut placerat. Duis facilisis, nisi sit amet dictum egestas, neque nulla elementum nibh, in ultrices mi magna nec metus.</p>
      <p>Duis arcu lacus, accumsan id lectus eu, condimentum tincidunt purus. Cras ac justo sed odio mattis gravida consectetur ac sapien. Integer eleifend enim et ipsum fermentum auctor. Quisque at porttitor velit. Aenean gravida nibh odio, eget tempus mauris semper at. In consectetur sed leo ut molestie. Sed pharetra urna quis turpis fringilla, ut posuere massa hendrerit. Proin pulvinar nibh augue, vel luctus elit aliquet non. Nunc elementum iaculis turpis eu interdum. Pellentesque non imperdiet magna, ut facilisis augue.</p>
      <p>Sincerely,</p>
    </div>
    <p class="sender">First Name Last Name<br>Position</p>
    <p class="footer">Rechtsanwaltskanzlei mit Schwerpunkt Strafrecht<br>Lindenweg 14 · 22587 Hamburg · jb@kanzlei-janbrueckner.de</p>
  </section>

  <!-- Badge card -->
  <section class="piece mini-front" aria-label="Karte Vorderseite klein">
    <p class="claim">KANN NUR BESSER WERDEN</p>
    <p class="phone">0176 . 48 21 90 35</p>
  </section>

  <!-- Small card back -->
  <section class="piece mini-back" aria-label="Karte Rückseite klein">
    <div class="brand">
      <span class="brand-dot"></span>
      <span class="brand-name">Jan Brückner</span>
      <span class="brand-role">Fachanwalt für Strafrecht</span>
      <p class="address">Rechtsanwaltskanzlei mit Schwerpunkt Strafrecht<br>Lindenweg 14 · 22587 Hamburg · jb@kanzlei-janbrueckner.de</p>
    </div>
  </section>

  <!-- Square flyer -->
  <section class="piece flyer" aria-label="Quadratischer Flyer">
    <p class="claim">KANN NUR BESSER WERDEN</p>
    <p class="owner">JAN BRÜCKNER</p>
  </section>

  <!-- Disc label -->
  <section class="piece disc" aria-label="CD-Label">
    <svg width="182" height="182" viewBox="0 0 182 182">
      <circle cx="91" cy="91" r="90" fill="#ffffff" stroke="#bdbdbd" stroke-width="1"/>
      <circle cx="91" cy="91" r="30" fill="#e2e2e2" stroke="#b5b5b5"/>
      <circle cx="91" cy="91" r="20" fill="#d0d0d0" stroke="#a8a8a8"/>
      <circle cx="91" cy="91" r="9" fill="#c8c8ca" stroke="#9a9a9a"/>
      <line x1="56" y1="140" x2="126" y2="140" stroke="#9a9a9a" stroke-width=".7"/>
      <line x1="56" y1="150" x2="126" y2="150" stroke="#9a9a9a" stroke-width=".7"/>
    </svg>
    <div class="brand">
      <span class="brand-dot"></span>
      <span class="brand-name">Jan Brückner</span>
    </div>
  </section>

  <!-- Envelopes -->
  <section class="piece envelope-back" aria-label="Umschlag Rückseite">
    <span class="flap"></span>
  </section>

  <section class="piece envelope" aria-label="Umschlag Vorderseite">
    <div class="brand">
      <span class="brand-dot"></span>
      <span class="brand-name">Jan Brückner</span>
    </div>
    <p class="sender-block"><strong>Musterfirma GmbH</strong><br>Addressee's name<br>Building number and street<br>Locality name (if required)<br>Post Town, Post Code<br><br>Tel: 123 456 7890<br>Fax: 234 567 8901<br>www.musterfirma.de</p>
    <svg class="window" viewBox="0 0 96 58">
      <path d="M0 6V0H6M90 0H96V6M96 52V58H90M6 58H0V52" fill="none" stroke="#999" stroke-width="1"/>
    </svg>
  </section>

</body>
</html>
```